New Business Card for Casual Beachfront Cafe

Quirky Beachfront Cafe at Moana, South Australia needs a DOUBLE SIDED business card to print on PrintHarbor.

Target Market(s)

Business Cards sit on the counter for Guests to take with them. Please view our website www.saltreefcafe.com.au to get a feel for the Cafe. You may also view our Instagram at @saltreefcafe

Industry/Entity Type

Cafe / Restaurant

Contact Information for Business Card

Information equivalent to: Breakfast, Lunch, Dinner, Coffee, Takeaway / 117 Parade Moana SA 5169 / Menu & Opening Hours: www.saltreefcafe.com.au / ph (08) 8461 9273

Requirements
Must have
• Information equivalent to: Breakfast, Lunch, Dinner, Coffee, Takeaway / 117 Parade Moana SA 5169 / Menu & Opening Hours: www.saltreefcafe.com.au / ph (08) 8461 9273
Nice to have
• Potentially some of our trademark colours (Cafe can be searched via Seekly)
Should not have
• Must NOT have image of the building. May have the logo provided on one side but not necessarily, depending on how you wish to design the card

```html
<!DOCTYPE html>
<html lang="en">
<head>
<meta charset="utf-8">
<title>Salt Reef Cafe – Business Card</title>
<link rel="stylesheet" href="https://fonts.googleapis.com/css2?family=Montserrat:wght@500;600;800;900&display=swap">
<style>
  :root {
    --page-bg: #e9e6e1;
    --card-white: #f4f4f2;
    --card-orange: #c2622a;
    --brand-blue: #1f4f8c;
    --brand-orange: #c8662c;
    --shadow: rgba(0, 0, 0, 0.18);
  }
  * { box-sizing: border-box; margin: 0; padding: 0; }
  html, body {
    width: 1200px;
    height: 900px;
    overflow: hidden;
    background: var(--page-bg);
    font-family: "Montserrat", Arial, sans-serif;
  }
  .sheet {
    width: 1200px;
    height: 900px;
    display: flex;
    flex-direction: column;
    align-items: center;
    justify-content: center;
    gap: 60px;
  }
  .card {
    width: 560px;
    height: 342px;
    border-radius: 4px;
    box-shadow: 0 10px 24px var(--shadow);
    position: relative;
  }
  .card--info {
    background: var(--card-white);
    padding: 40px 22px 36px 34px;
    display: flex;
    flex-direction: column;
  }
  .headline {
    text-align: center;
    font-weight: 900;
    text-transform: uppercase;
    line-height: 1.1;
    white-space: nowrap;
  }
  .headline__top {
    display: block;
    color: var(--brand-blue);
    font-size: 25px;
    letter-spacing: 0.5px;
  }
  .headline__bottom {
    display: block;
    color: var(--brand-orange);
    font-size: 22px;
  }
  .intro {
    margin-top: 8px;
    text-align: center;
    color: var(--brand-blue);
    font-weight: 500;
    font-size: 13px;
    line-height: 1.35;
  }
  .contact {
    margin-top: auto;
    list-style: none;
    color: var(--brand-blue);
    font-weight: 600;
    font-size: 16px;
    line-height: 1.4;
  }
  .card--brand {
    background: var(--card-orange);
    display: flex;
    align-items: center;
    justify-content: center;
  }
  .brand-name {
    color: var(--brand-blue);
    font-weight: 800;
    font-size: 40px;
    line-height: 1;
    text-transform: uppercase;
    text-align: center;
    white-space: nowrap;
  }
</style>
</head>
<body>
  <main class="sheet">
    <section class="card card--info" aria-label="Card back">
      <h1 class="headline">
        <span class="headline__top">Retro Beach Vibe</span>
        <span class="headline__bottom">With Delicious Homestyle Food!</span>
      </h1>
      <p class="intro">Visit us for breakfast, lunch &amp; dinner or just a cup of coffee!<br>Check our menu online &amp; order via website or phone.</p>
      <ul class="contact">
        <li>117 Parade Moana SA 5169</li>
        <li>www.saltreefcafe.com.au</li>
        <li>(08) 8461 9273</li>
      </ul>
    </section>
    <section class="card card--brand" aria-label="Card front">
      <p class="brand-name">Salt Reef Cafe</p>
    </section>
  </main>
</body>
</html>
```